Portal Panel Medic need professional looking business card printed on plastic, Commericial, Industri

We are family owned and operated garage door company in Indianapolis, Indiana. We sale service and install dock equipment, doors, operators. We are looking to expand our commercial/ industrial division. We also service all residential doors and operators. We are looking for a business that stands out of the crowd. We are committed to have the best customer service in the industry.

Target Market(s)

National and local general contractors, National/ Corpate service accounts,

Industry/Entity Type

Business Service

Contact Information for Business Card

To be printed on plastic stock

Font styles to use
Sans Serif

Colors
ffffff
f04a50
ec1f27

Requirements
Must have
• Name, website,email, phone number, position.
Nice to have
• A standout professional design

```html
<!DOCTYPE html>
<html lang="en">
<head>
<meta charset="utf-8">
<title>Portal Panel Medic – Business Card</title>
<link rel="stylesheet" href="https://fonts.googleapis.com/css2?family=Oswald:wght@500&family=Open+Sans:wght@400;600&display=swap">
<style>
  :root {
    --red: #ec1f27;
    --red-soft: #f04a50;
    --ink: #1a1a1a;
    --text: #2b2b2b;
    --card: #eef0f1;
    --card-edge: #d9dcde;
    --stage: #f6f6f4;
    --art-light: #e7e1da;
    --art-dark: #a58f7e;
  }
  * { box-sizing: border-box; margin: 0; padding: 0; }
  html, body { width: 1200px; height: 527px; overflow: hidden; background: var(--stage); }
  .canvas { position: relative; width: 1200px; height: 527px; }

  .card {
    position: absolute; top: 146px; width: 428px; height: 258px;
    background: var(--card); border: 1px solid var(--card-edge);
    border-radius: 3px; overflow: hidden;
    box-shadow: 0 6px 18px rgba(0,0,0,0.08);
  }
  .card--front { left: 86px; }
  .card--back { left: 686px; }

  .mascot-area {
    position: absolute;
    background: linear-gradient(160deg, var(--art-light), var(--art-dark));
    border-radius: 4px; opacity: 0.85;
  }

  /* shared company name: plain text, one colour, one weight */
  .company-name {
    position: absolute;
    font-family: "Open Sans", sans-serif; font-weight: 600;
    color: var(--ink); letter-spacing: 0.2px;
  }

  /* front */
  .card--front .mascot-area { left: 92px; top: 68px; width: 52px; height: 110px; }
  .card--front .company-name {
    left: 156px; top: 96px; width: 200px;
    font-size: 24px; line-height: 1.25;
  }
  .front-web {
    position: absolute; left: 0; right: 0; top: 232px;
    display: flex; align-items: center; justify-content: center; gap: 10px;
    font: 400 11.5px "Open Sans", sans-serif; color: var(--text);
  }
  .front-web::before, .front-web::after {
    content: ""; width: 62px; height: 2px; background: var(--red);
  }

  /* back */
  .card--back .mascot-area { left: 0; top: 22px; width: 214px; height: 228px; border-radius: 4px 60px 4px 4px; }
  .card--back .company-name {
    left: 222px; top: 38px; width: 190px; text-align: right;
    font-size: 19px; line-height: 1.2;
  }
  .person { position: absolute; right: 17px; top: 134px; text-align: right; }
  .person-name { font: 500 17px/1.2 "Oswald", sans-serif; color: var(--ink); }
  .person-role { font: 400 11px/1.5 "Open Sans", sans-serif; color: var(--red-soft); }
  .contacts {
    position: absolute; right: 17px; top: 190px; list-style: none;
    font: 400 10.5px/17px "Open Sans", sans-serif; color: var(--text); text-align: right;
  }
  .contacts li { display: flex; align-items: center; justify-content: flex-end; gap: 6px; }
  .contacts svg { width: 9px; height: 9px; fill: var(--red); flex: none; }
  .contacts .accent { color: var(--red); }
  .card-bar { position: absolute; left: 0; right: 0; bottom: 6px; height: 6px; display: flex; }
  .card-bar .bar-red { width: 146px; background: var(--red); }
  .card-bar .bar-dark { flex: 1; background: var(--ink); }
</style>
</head>
<body>
<main class="canvas">
  <section class="card card--front">
    <div class="mascot-area" role="img" aria-label="Cartoon mascot of an elderly doctor with stethoscope"></div>
    <div class="company-name">Portal Panel Medic</div>
    <div class="front-web">www.portalpanelmedic.com</div>
  </section>

  <section class="card card--back">
    <div class="mascot-area" role="img" aria-label="Cartoon mascot of an elderly doctor holding a stethoscope and a book"></div>
    <div class="company-name">Portal Panel Medic</div>
    <div class="person">
      <div class="person-name">Jordan Lee Parker</div>
      <div class="person-role">Managing Director</div>
    </div>
    <ul class="contacts">
      <li><span>(317) 555-0142</span>
        <svg viewBox="0 0 10 10" aria-hidden="true"><path d="M1 3.5C1 2 2.5 1.5 5 1.5S9 2 9 3.5L7.5 4 7 3H3L2.5 4ZM2.5 5h5L8.5 8.5h-7Z"/></svg></li>
      <li><span>jordan@portalpanelmedic.com</span>
        <svg viewBox="0 0 10 10" aria-hidden="true"><path d="M1 2.5h8v5H1Z M1 2.5 5 5.5 9 2.5" stroke="#fff" stroke-width="0.8"/></svg></li>
      <li><span>www.<span class="accent">portalpanelmedic</span>.com</span>
        <svg viewBox="0 0 10 10" aria-hidden="true"><circle cx="5" cy="5" r="4.2"/><path d="M1 5h8M5 0.8v8.4M5 0.8C3 3 3 7 5 9.2M5 0.8C7 3 7 7 5 9.2" stroke="#fff" stroke-width="0.6" fill="none"/></svg></li>
    </ul>
    <div class="card-bar"><span class="bar-red"></span><span class="bar-dark"></span></div>
  </section>
</main>
</body>
</html>
```